Need UI design of one scene of a word game app

We need your help to design a game play scene of a word game app for birch wareloft. This is just one scene of the whole app. We may need design of more scenes of the game in the future.

Here is the list of items we need:
1.The overall UI design of this scene and the pop-up window within the scene.
2.The button designs of this scene.
3.One ice drawing around the frame.
4.One lightning animation (with several images) around the button.
5.This scene will support both zorvex and kelo. So the screen size will be 640x1196 and 1536x2048.

Please refer to the pdf file attached for details.

Thank you.

```html
<!DOCTYPE html>
<html lang="en">
<head>
<meta charset="utf-8">
<title>Word Game – Options Scene</title>
<link rel="stylesheet" href="https://fonts.googleapis.com/css2?family=Fredoka:wght@600;700&family=Inter:wght@400;500&display=swap">
<style>
  :root{
    --page-bg:#eef0f2;
    --screen-edge:#1d1d1f;
    --status-bg:#fdfbf4;
    --status-text:#2a2a2a;
    --play-bg:#fdf3d1;
    --sidebar-bg:#cfc3a5;
    --sidebar-text:#ffffff;
    --sidebar-outline:#8f8366;
    --panel-bg:#f6e2a9;
    --panel-rim:#d9ccaa;
    --green-top:#b6ea58;
    --green-mid:#8fd73a;
    --green-low:#68bd22;
    --green-edge:#4e9a18;
    --green-text-shadow:#3f7f14;
    --orange-top:#ffd23a;
    --orange-low:#f5a511;
    --orange-edge:#d1840a;
    --orange-text-shadow:#b36b06;
    --button-rim:#ffffff;
    --action-band:#00b0da;
    --ad-bg:#ffffff;
    --ad-text:#c4c4c4;
    --bolt:#b69a10;
    --flame:#c4161c;
    --gem:#2db2d6;
    --gem-light:#7fd9ef;
  }
  *{box-sizing:border-box;margin:0;padding:0}
  html,body{width:1024px;height:1200px;overflow:hidden;background:var(--page-bg)}
  body{position:relative;font-family:"Fredoka",sans-serif}

  .screen{position:absolute;left:192px;top:32px;width:640px;height:1136px;
    border:6px solid var(--screen-edge);overflow:hidden;background:var(--play-bg)}

  .status-bar{position:absolute;left:0;top:0;width:100%;height:40px;background:var(--status-bg);
    font-family:"Inter",sans-serif;font-size:21px;color:var(--status-text);display:flex;align-items:center;padding:0 12px}
  .status-carrier{display:flex;align-items:center;gap:6px;width:200px}
  .signal-dots{display:flex;gap:3px}
  .signal-dots i{width:9px;height:9px;border-radius:50%;background:var(--status-text);display:block}
  .status-time{flex:1;text-align:center}
  .status-right{display:flex;align-items:center;gap:8px;width:200px;justify-content:flex-end}

  .play-area{position:absolute;left:0;top:40px;width:510px;height:832px;background:var(--play-bg)}
  .sidebar{position:absolute;left:510px;top:40px;width:118px;height:832px;background:var(--sidebar-bg)}

  .options-panel{position:absolute;left:84px;top:130px;width:344px;height:568px;
    background:var(--panel-bg);border:8px solid var(--panel-rim);border-radius:48px}
  .panel-title{position:absolute;left:120px;top:100px;width:268px;height:66px;
    background:linear-gradient(var(--green-top),var(--green-low));border-bottom:6px solid var(--button-rim);
    border-radius:4px 4px 10px 10px;display:flex;align-items:center;justify-content:center;
    color:#fff;font-weight:700;font-size:34px;letter-spacing:1px;text-shadow:0 3px 0 var(--green-text-shadow)}

  .game-button{position:absolute;width:248px;height:80px;border-radius:26px;
    border:4px solid var(--button-rim);border-top-width:2px;
    background:linear-gradient(var(--green-top) 0%,var(--green-mid) 55%,var(--green-low) 100%);
    box-shadow:0 5px 0 var(--panel-rim),inset 0 -8px 0 var(--green-edge);
    display:flex;align-items:center;justify-content:center;
    color:#fff;font-weight:700;font-size:34px;letter-spacing:1px;
    text-shadow:0 3px 0 var(--green-text-shadow),0 0 2px var(--green-text-shadow)}
  .game-button::before{content:"";position:absolute;left:16px;top:8px;width:26px;height:10px;border-radius:50%;background:rgba(255,255,255,.55)}
  .game-button::after{content:"";position:absolute;right:14px;bottom:16px;width:12px;height:8px;border-radius:50%;background:rgba(255,255,255,.7)}
  .game-button.is-primary{background:linear-gradient(var(--orange-top),var(--orange-low));
    box-shadow:0 5px 0 var(--panel-rim),inset 0 -8px 0 var(--orange-edge);
    text-shadow:0 3px 0 var(--orange-text-shadow),0 0 2px var(--orange-text-shadow)}
  .btn-resume{left:130px;top:238px}
  .btn-restart{left:132px;top:362px}
  .btn-exit{left:134px;top:488px}
  .btn-sound{left:136px;top:614px}

  .pause-button{position:absolute;left:20px;top:20px;width:84px;height:82px;border-radius:26px;
    border:3px solid var(--button-rim);background:linear-gradient(var(--green-top),var(--green-low));
    box-shadow:inset 0 -7px 0 var(--green-edge),0 4px 0 #b3a78a;display:flex;align-items:center;justify-content:center;gap:8px}
  .pause-button i{display:block;width:14px;height:40px;border-radius:5px;background:#fff}

  .stat{position:absolute;left:0;width:100%;text-align:center;color:var(--sidebar-text);font-weight:700;
    text-shadow:0 2px 0 var(--sidebar-outline),0 0 3px var(--sidebar-outline)}
  .stat-label{font-size:24px}
  .stat-value{font-size:42px}
  .stat-count{font-size:24px}
  .power-icon{position:absolute;left:50%;transform:translateX(-50%)}

  .action-band{position:absolute;left:0;top:872px;width:100%;height:140px;background:var(--action-band)}
  .action-band .game-button{width:244px;height:92px;top:22px;font-size:42px;box-shadow:inset 0 -8px 0 var(--green-edge),0 5px 0 #0d87a8}
  .btn-word{left:58px}
  .btn-clear{left:340px}

  .ad-slot{position:absolute;left:0;top:1012px;width:100%;height:112px;background:var(--ad-bg);
    display:flex;align-items:center;justify-content:center;color:var(--ad-text);font-weight:700;font-size:38px}
</style>
</head>
<body>
  <main class="screen">
    <header class="status-bar">
      <div class="status-carrier">
        <span class="signal-dots"><i></i><i></i><i></i><i></i><i></i></span>
        <span>Telvora</span>
        <svg width="22" height="16" viewBox="0 0 22 16" aria-hidden="true"><path d="M1 5a15 15 0 0 1 20 0M4.5 8.5a10 10 0 0 1 13 0M8 12a5 5 0 0 1 6 0" fill="none" stroke="#2a2a2a" stroke-width="2.2" stroke-linecap="round"/></svg>
      </div>
      <div class="status-time">9:23 AM</div>
      <div class="status-right">
        <svg width="16" height="16" viewBox="0 0 16 16" aria-hidden="true"><path d="M15 1 1 7l7 1 1 7z" fill="#2a2a2a"/></svg>
        <span>66%</span>
        <svg width="46" height="20" viewBox="0 0 46 20" aria-hidden="true"><rect x="1" y="2" width="40" height="16" rx="3" fill="none" stroke="#2a2a2a" stroke-width="2"/><rect x="4" y="5" width="24" height="10" fill="#2a2a2a"/><rect x="42" y="7" width="3" height="6" fill="#2a2a2a"/></svg>
      </div>
    </header>

    <section class="play-area">
      <div class="options-panel"></div>
      <div class="panel-title">OPTIONS</div>
      <div class="game-button is-primary btn-resume">RESUME</div>
      <div class="game-button btn-restart">RESTART</div>
      <div class="game-button btn-exit">EXIT</div>
      <div class="game-button btn-sound">SOUND</div>
    </section>

    <aside class="sidebar">
      <div class="pause-button"><i></i><i></i></div>
      <div class="stat stat-label" style="top:140px">LETTER</div>
      <div class="stat stat-value" style="top:168px">45</div>
      <div class="stat stat-label" style="top:244px">LEVEL</div>
      <div class="stat stat-value" style="top:272px">99</div>

      <svg class="power-icon" style="top:350px" width="76" height="80" viewBox="0 0 76 80" aria-label="Lightning power-up"><path d="M30 4h42L48 32h18L8 76l18-36H8z" fill="var(--bolt)" stroke="#fff" stroke-width="4" stroke-linejoin="round"/></svg>
      <div class="stat stat-count" style="top:438px">X1</div>

      <svg class="power-icon" style="top:490px" width="80" height="96" viewBox="0 0 80 96" aria-label="Fire power-up"><path d="M40 4c4 18 30 30 30 56a30 30 0 0 1-60 0c0-14 8-22 14-28 0 10 4 16 10 18C30 36 32 18 40 4zM40 92c-10 0-14-8-12-16 2 6 6 8 10 8-2-10 4-16 6-22 4 8 10 14 10 20 0 6-6 10-14 10z" fill="var(--flame)" fill-rule="evenodd"/></svg>
      <div class="stat stat-count" style="top:600px">X1</div>

      <svg class="power-icon" style="top:660px" width="84" height="72" viewBox="0 0 84 72" aria-label="Diamond power-up"><path d="M20 4h44l16 20-38 44L4 24z" fill="var(--gem)" stroke="#fff" stroke-width="4" stroke-linejoin="round"/><path d="M20 4 32 24h20L64 4M4 24h76" fill="none" stroke="var(--gem-light)" stroke-width="3"/></svg>
      <div class="stat stat-count" style="top:756px">X1</div>
    </aside>

    <section class="action-band">
      <div class="game-button btn-word">WORD</div>
      <div class="game-button btn-clear">CLEAR</div>
    </section>

    <footer class="ad-slot">AD</footer>
  </main>
</body>
</html>
```